Wendrik - 3 Etiketten für naturbelassenes Speiseöl - Leinöl, Leindotteröl und Rapsöl
Zielgruppe
Wir sind ein junges Startup mit der Ziel, die besten, gesündesten Omega3-Öle in bester handwerklicher Qualität anzubieten. Vor allem soll das folgende Unterscheidungsmerkmal unsere Marke verkörpern: in Supermärkten und Discountern gibt es überwiegend denaturierte Öle, das heißt extrahierte und raffinierte Öle. Dadurch sind diese zwar länger haltbar, jedoch wertlos für den Körper. Wir wollen Öle voller Naturkraft anbieten und lassen daher die bei Ölpressung entstehenden Schwebestoffe im Form gesunder sekundärer Pflanzenstoffe bewusst im Öl und filtern diese nicht heraus.
Unser Markenname - Wendrik … mit dem Slogan ' Wendrik sein heißt für uns: dynamisch, kraftvoll, vital, frohen Mutes und voller Lebendigkeit - genauso ist unser Öl. Frisch gepresst in bester handwerklicher Qualität, naturbelassen voller gesunder sekundärer Pflanzenstoffe und reich an lebenswichtigen Omega3-Fettsäuren.'
Fokus der Wendrik-Ölmanufakur: echtes Handwerk, beste Qualität, pure Leidenschaft, wahre Nachhaltigkeit und authentische Regionalität!
Aufgabenstellung
In Summe benötigen wir 3 Etiketten für 3 verschiedene Speiseöle: Leinöl, Leindotteröl und Rapsöl.
Für diese drei Öle benötigen wir das Design kreativer, ansprechender Etiketten mit folgenden Prämissen:
A. Etiketten im Tafelkreidestil (Chalk-Handlettering): gemäß unser Vision wollen wir die besten, gesündesten Omega3-Öle in bester handwerklicher Qualität anbieten - diesen Aspekt soll das Look&Feel der Ölflasche samt Etikett verkörpern. Abgefüllt wird unser Öl in hochwertige mattschwarze Steinzeugölflaschen mit Holzkorkverschluss (siehe beigefügtes Bild). Durch das matte schwarz der Ölfalsche soll grundsätzlich das Etiketten-Design im Tafelkreidestil (Chalk-Handlettering) mit einem kreativen Mix aus schönen (gut lesbaren) Schriften und graphischen Elementen sein. Das Endprodukt des Etiketts soll ein transparenter Aufkleber sein, der auf die Flasche geklebt wird.
Maximale Größe des Etiketts: 200ml Flasche max. 13,5 cm Höhe x max. 17 cm Breite
Hinweis: das Etikett soll für die Größe der 200ml Flasche konzipiert werden, jedoch idealerweise so skalierbar sein, daß es auch auf die Größe einer 500 ml-Flasche angepasst werden kann; Größe der 500 ml Flasche max. Höhe 17 cm x max. Breite 21,5 cm
B. Pflanzen-/Saatenzweig als graphisches Unterscheidungsmerkmal des Öls: idealerweise wird das jeweilige Öl (Rapsöl, Leinöl und Leindotteröl) mit einem graphischen Pflanzenzweig der jeweiligen Ölsaat gekennzeichnet.
C. Was macht dies Öl so wertvoll? - die wichtigen und wertvollsten Inhaltsstoffe des jeweiligen Öls sollen herausgestellt werden.
Bein Leinöl und Leindotteröl ist dies vor allem der hohe Gehalt an Omega3-Fettsäuren - dies macht das Öl so besonders wertvoll
Graphisches Textelement mit 'Der Omega3 Booster fur den Körper' (oder der “Powerlieferant” für Omega 3)
Gut für: Herz-Kreislaufszsystem stärken
Gehirnleistung steigern
Blu..

```html
<!DOCTYPE html>
<html lang="de">
<head>
<meta charset="utf-8">
<title>Wendrik – Etiketten Leinöl, Leindotteröl, Rapsöl</title>
<link rel="stylesheet" href="https://fonts.googleapis.com/css2?family=Rubik+Dirt&family=Oswald:wght@400&display=swap">
<style>
  :root {
    --page: #ffffff;
    --label-ground: #1d1b1c;
    --label-ground-edge: #141213;
    --chalk: #f4f2ee;
    --chalk-cream: #eedca0;
    --badge-green: #6f9a2c;
    --sketch-grey: #8e8c8a;
  }
  * { margin: 0; padding: 0; box-sizing: border-box; }
  html, body {
    width: 1200px;
    height: 1039px;
    overflow: hidden;
    background: var(--page);
  }
  .label-set {
    position: relative;
    width: 1200px;
    height: 1039px;
  }
  .label {
    position: absolute;
    top: 193px;
    width: 284px;
    height: 786px;
    border-radius: 10px;
    background: linear-gradient(90deg, var(--label-ground-edge) 0%, var(--label-ground) 30%, var(--label-ground) 70%, var(--label-ground-edge) 100%);
    color: var(--chalk);
  }
  .label--lein { left: 116px; }
  .label--leindotter { left: 460px; }
  .label--raps { left: 800px; }

  .brand {
    position: absolute;
    top: 88px;
    left: 90px;
    display: flex;
    align-items: center;
    gap: 7px;
  }
  .brand__dot {
    width: 14px;
    height: 14px;
    border-radius: 50%;
    border: 1.5px solid var(--chalk);
  }
  .brand__name {
    font-family: "Oswald", sans-serif;
    font-weight: 400;
    font-size: 22px;
    line-height: 26px;
    letter-spacing: 0.5px;
    color: var(--chalk);
  }

  .oil-name {
    position: absolute;
    writing-mode: vertical-rl;
    transform: rotate(180deg);
    font-family: "Rubik Dirt", sans-serif;
    font-weight: 400;
    font-size: 48px;
    line-height: 44px;
    letter-spacing: 2px;
    color: var(--chalk);
    white-space: nowrap;
  }
  .oil-name__accent { color: var(--chalk-cream); }
  .label--lein .oil-name { left: 121px; top: 244px; }
  .label--leindotter .oil-name { left: 126px; top: 241px; font-size: 45px; letter-spacing: 1px; }
  .label--raps .oil-name { left: 129px; top: 251px; }

  .seal {
    position: absolute;
    width: 55px;
    height: 55px;
    border-radius: 50%;
    background: var(--badge-green);
  }
  .label--lein .seal { left: 170px; top: 296px; }
  .label--leindotter .seal { left: 176px; top: 295px; }
  .label--raps .seal { left: 173px; top: 293px; }

  .plant-sketch {
    position: absolute;
    border-radius: 30px;
    background: linear-gradient(180deg, rgba(142,140,138,0.35), rgba(142,140,138,0.12));
  }
  .label--lein .plant-sketch { left: 50px; top: 317px; width: 70px; height: 375px; }
  .label--leindotter .plant-sketch { left: 46px; top: 323px; width: 72px; height: 369px; }
  .label--raps .plant-sketch { left: 44px; top: 317px; width: 74px; height: 369px; }

  .qualities {
    position: absolute;
    list-style: none;
    font-family: "Oswald", sans-serif;
    font-weight: 400;
    font-size: 14px;
    line-height: 18px;
    color: var(--chalk);
  }
  .qualities li + li { margin-top: 11px; }
  .label--lein .qualities { left: 132px; top: 466px; }
  .label--leindotter .qualities { left: 180px; top: 362px; }
  .label--raps .qualities { left: 132px; top: 464px; }

  .volume {
    position: absolute;
    font-family: "Oswald", sans-serif;
    font-weight: 400;
    font-size: 26px;
    line-height: 30px;
    color: var(--chalk);
  }
  .label--lein .volume { left: 132px; top: 722px; }
  .label--leindotter .volume { left: 180px; top: 714px; }
  .label--raps .volume { left: 132px; top: 722px; }
</style>
</head>
<body>
<main class="label-set">

  <section class="label label--lein">
    <div class="brand"><span class="brand__dot"></span><span class="brand__name">Wendrik</span></div>
    <div class="plant-sketch" role="img" aria-label="Kreidezeichnung eines Leinzweigs mit Blüten"></div>
    <h2 class="oil-name">LEINÖL</h2>
    <div class="seal" role="img" aria-label="Omega-3 Siegel"></div>
    <ul class="qualities">
      <li>dynamisch</li>
      <li>vital</li>
      <li>kraftvoll</li>
      <li>frisch<br>gepresst</li>
      <li>naturbelassen</li>
      <li>reich an<br>Omega3<br>Fettsäuren</li>
    </ul>
    <p class="volume">200ml</p>
  </section>

  <section class="label label--leindotter">
    <div class="brand"><span class="brand__dot"></span><span class="brand__name">Wendrik</span></div>
    <div class="plant-sketch" role="img" aria-label="Kreidezeichnung eines Leindotterzweigs mit Blüten"></div>
    <h2 class="oil-name">LEIN<span class="oil-name__accent">DOTTER</span>ÖL</h2>
    <div class="seal" role="img" aria-label="Omega-3 Siegel"></div>
    <ul class="qualities">
      <li>dynamisch</li>
      <li>vital</li>
      <li>kraftvoll</li>
      <li>frisch<br>gepresst</li>
      <li>naturbelassen</li>
      <li>reich an<br>Omega3<br>Fettsäuren</li>
    </ul>
    <p class="volume">200ml</p>
  </section>

  <section class="label label--raps">
    <div class="brand"><span class="brand__dot"></span><span class="brand__name">Wendrik</span></div>
    <div class="plant-sketch" role="img" aria-label="Kreidezeichnung eines Rapszweigs mit Blüten"></div>
    <h2 class="oil-name">RAPSÖL</h2>
    <div class="seal" role="img" aria-label="Omega-3 Siegel"></div>
    <ul class="qualities">
      <li>dynamisch</li>
      <li>vital</li>
      <li>kraftvoll</li>
      <li>frisch<br>gepresst</li>
      <li>naturbelassen</li>
      <li>reich an<br>Omega3<br>Fettsäuren</li>
    </ul>
    <p class="volume">200ml</p>
  </section>

</main>
</body>
</html>
```